Expedition Cruise Sales Website for the Polar Regions (Antarctica & Arctic)

This will be a website for selling cruises.
This site should have a homepage, a ship page, destinations, and itineraries.
I have created a file specifying each page, and it is attached.
Pages:
1. Home
2. Cruise Lines
- 2.1 Ships
3. Destinations
- 3.1 Region - 3.2 Country - 3.3 City
4. Itineraries
- 4.1 Itinerary
5. Blog / Travel Tips 6. About Us
7. Contact
Please take a look on the attached pdf
Target Market(s)
Expedition Travelers
Coding
Coded - Design and coding required
Number of Pages Required
5+ page

```html
<!DOCTYPE html>
<html lang="en">
<head>
<meta charset="utf-8">
<title>Polarvia.co — Expedition Cruises</title>
<link href="https://fonts.googleapis.com/css2?family=Outfit:wght@400;500;600;700;800&family=Roboto:wght@400;500;700&display=swap" rel="stylesheet">
<style>
:root{
  --blue:#2f6db5;
  --ink:#1d1f2c;
  --text:#3a3d48;
  --muted:#6b6f7a;
  --navy:#2b2a6b;
  --navy-deep:#25245f;
  --navy-soft:#3a3980;
  --white:#ffffff;
  --card-shadow:0 4px 14px rgba(20,30,60,.12);
}
*{box-sizing:border-box;margin:0;padding:0}
html,body{width:1200px;height:3558px;overflow:hidden}
body{position:relative;font-family:'Outfit',sans-serif;color:var(--text);background:var(--white)}

/* Hero */
.hero{position:absolute;left:0;top:0;width:1200px;height:640px;overflow:hidden}
.hero-photo{position:absolute;inset:0;background:linear-gradient(100deg,#5f7f9c 0%,#8aa4bc 30%,#c6d3de 55%,#e3e9ee 75%,#f4f6f8 100%)}
.hero-wave{position:absolute;left:0;bottom:0;width:1200px;height:100px}
.logo{position:absolute;left:144px;top:14px;width:170px;text-align:center}
.logo-mark{width:44px;height:44px;border-radius:50%;background:var(--blue);margin:8px auto 6px}
.logo-name{font-size:32px;font-weight:600;color:var(--blue);line-height:1.2}
.nav{position:absolute;top:34px;left:432px;display:flex;gap:34px;font-size:15px;color:var(--ink)}
.nav a{text-decoration:none;color:inherit}
.nav .active{color:var(--blue)}
.hero-kicker{position:absolute;left:0;width:1546px;text-align:center;top:212px;font-size:31px;font-weight:700;color:var(--blue)}
.hero-title{position:absolute;left:0;width:1546px;text-align:center;top:256px;font-size:74px;font-weight:700;color:var(--ink);line-height:1}
.search{position:absolute;left:507px;top:351px;width:528px;height:52px;border-radius:26px;background:var(--white);box-shadow:0 2px 8px rgba(0,0,0,.12)}
.search span{position:absolute;left:25px;top:16px;font-size:14px;color:var(--ink)}
.search-btn{position:absolute;right:4px;top:4px;width:152px;height:44px;border-radius:22px;background:var(--blue);color:var(--white);font-size:14px;font-weight:600;text-align:center;line-height:44px}
.arrow{position:absolute;width:40px;height:40px;border-radius:50%;background:rgba(235,238,242,.9);display:flex;align-items:center;justify-content:center}
.arrow svg{width:12px;height:12px}

/* Section titles */
.sec-title{position:absolute;left:0;width:1200px;text-align:center;font-size:40px;font-weight:700;color:var(--ink);letter-spacing:.5px;line-height:1.2}
.sec-title em{font-style:normal;color:var(--blue)}

/* Offers */
.offer{position:absolute;top:783px;width:427px}
.offer-img{height:251px;border-radius:22px}
.offer h3{margin:16px 0 0 32px;font-size:24px;font-weight:600;color:var(--ink);display:inline-block;padding-bottom:8px;border-bottom:2px solid var(--blue)}
.offer p{margin:12px 0 0 32px;width:370px;font-size:15px;line-height:28px;color:var(--text)}
.offer .price{margin:6px 0 0 32px;font-size:25px;font-weight:700;color:var(--blue)}

/* Destinations */
.dest-band{position:absolute;left:0;top:1280px;width:1200px;height:536px;background:linear-gradient(180deg,#dfe9f2 0%,#f2f6f9 18%,#9fd8e3 40%,#5fc6d4 55%,#a9dfe6 75%,#eef2f4 100%)}
.dest-lead{position:absolute;left:235px;width:730px;top:1393px;text-align:center;font-size:15px;line-height:24px;color:var(--ink)}
.dest{position:absolute;top:1465px;width:292px}
.dest-img{height:227px;border-radius:4px}
.dest h4{text-align:center;margin-top:14px;font-size:19px;font-weight:600;color:var(--ink)}

/* Cruise lines */
.line-card{position:absolute;width:442px;height:194px;background:var(--white);border-radius:6px;box-shadow:var(--card-shadow)}
.line-img{position:absolute;left:14px;top:13px;width:152px;height:168px}
.line-card h4{position:absolute;left:187px;top:28px;font-size:20px;font-weight:600;color:var(--ink)}
.line-card p{position:absolute;left:187px;top:64px;width:225px;font-size:12.5px;line-height:22px;color:var(--muted)}
.line-card a{position:absolute;left:187px;top:139px;font-size:14px;font-weight:600;color:var(--blue);text-decoration:underline}
.btn-more{position:absolute;left:498px;top:2418px;width:204px;height:42px;border-radius:21px;background:var(--blue);color:var(--white);font-size:14px;font-weight:600;text-align:center;line-height:42px}

/* Testimonials */
.testi-band{position:absolute;left:0;top:2460px;width:1200px;height:700px;background:linear-gradient(180deg,#ffffff 0%,#e6e7eb 14%,#dfe0e5 32%,#eaebee 50%,#ededf0 100%)}
.testi{position:absolute;top:2763px;width:362px;height:219px;background:var(--white);border-radius:10px;box-shadow:var(--card-shadow)}
.testi .stars{position:absolute;left:70px;top:28px}
.testi p{position:absolute;left:70px;top:52px;width:268px;font-size:16px;line-height:24px;text-align:justify;color:var(--ink)}
.testi .who{position:absolute;left:70px;top:178px;font-size:19px;font-weight:600;color:var(--ink)}
.testi .who small{font-size:13px;font-weight:400;color:var(--muted);margin-left:8px}
.avatar{position:absolute;top:2810px;width:124px;height:124px;border-radius:50%}
.chev{position:absolute;top:2860px;width:24px;height:30px}

/* Footer */
.footer-wave{position:absolute;left:0;top:3070px;width:1200px;height:100px}
.footer{position:absolute;left:0;top:3168px;width:1200px;height:390px;background:var(--navy);color:var(--white);font-family:'Roboto',sans-serif}
.footer h5{position:absolute;font-size:19px;font-weight:500;line-height:28px;letter-spacing:.3px}
.email-field{position:absolute;left:144px;top:143px;width:270px;height:42px;border:1px solid rgba(255,255,255,.75);font-size:13px;padding:13px 17px}
.email-field svg{position:absolute;right:10px;top:12px}
.social{position:absolute;top:214px;width:24px;height:24px;border-radius:50%;background:var(--navy-soft)}
.social.on{width:30px;height:30px;top:211px;background:var(--white)}
.contact-item{position:absolute;left:504px}
.contact-item strong{display:block;font-size:15px;font-weight:500;margin-left:42px}
.contact-item span{display:block;font-size:12px;margin:5px 0 0 42px}
.contact-item svg{position:absolute;left:0;top:2px}
.links{position:absolute;top:136px;font-size:15px;line-height:32px;list-style:none}
.links li::before{content:"»";margin-right:14px}
.copyright{position:absolute;left:0;top:312px;width:1200px;height:78px;background:var(--navy-deep);text-align:center;font-size:15px;line-height:70px}
</style>
</head>
<body>

<!-- Hero -->
<header class="hero">
  <div class="hero-photo" role="img" aria-label="Couple celebrating on the bow of a sailing boat at sea"></div>
  <svg class="hero-wave" viewBox="0 0 1200 100" preserveAspectRatio="none"><path d="M0 60 C120 110 280 110 400 70 C520 30 600 70 720 70 C860 70 960 10 1200 20 L1200 100 L0 100 Z" fill="#ffffff"/></svg>
  <div class="logo"><div class="logo-mark"></div><div class="logo-name">Polarvia.co</div></div>
  <nav class="nav">
    <a class="active" href="#">Home</a><a href="#">Cruise Lines</a><a href="#">Destinations</a><a href="#">Itineraries</a><a href="#">Blog</a><a href="#">About Us</a><a href="#">Contact</a>
  </nav>
  <div class="hero-kicker">Welcome To</div>
  <h1 class="hero-title">Polarvia</h1>
  <div class="search"><span>Cruise Search</span><div class="search-btn">Search Now</div></div>
  <div class="arrow" style="left:52px;top:284px"><svg viewBox="0 0 12 12"><path d="M8 1 L3 6 L8 11" stroke="#333" stroke-width="1.6" fill="none"/></svg></div>
  <div class="arrow" style="left:1108px;top:284px"><svg viewBox="0 0 12 12"><path d="M4 1 L9 6 L4 11" stroke="#333" stroke-width="1.6" fill="none"/></svg></div>
</header>

<!-- Featured offers -->
<h2 class="sec-title" style="top:712px">FEATURED <em>OFFERS</em></h2>
<div class="arrow" style="left:52px;top:888px"><svg viewBox="0 0 12 12"><path d="M8 1 L3 6 L8 11" stroke="#333" stroke-width="1.6" fill="none"/></svg></div>
<div class="arrow" style="left:1108px;top:888px"><svg viewBox="0 0 12 12"><path d="M4 1 L9 6 L4 11" stroke="#333" stroke-width="1.6" fill="none"/></svg></div>
<article class="offer" style="left:152px">
  <div class="offer-img" role="img" aria-label="Cruise ship sailing across deep blue open sea" style="background:linear-gradient(180deg,#4a86c4 0%,#1f5fa8 40%,#0f4a92 100%)"></div>
  <h3>Best Antarctic Cruises</h3>
  <p>Lorem ipsum dolor sit amet, consectetur adipiscing sed do eiusmod tempor incididunt ut</p>
  <div class="price">$50.00</div>
</article>
<article class="offer" style="left:621px">
  <div class="offer-img" role="img" aria-label="Small expedition boat on calm sea under a cloudy sky" style="background:linear-gradient(180deg,#cfdbe6 0%,#e9eef2 45%,#6a8fae 60%,#33628f 100%)"></div>
  <h3>Top Galápagos Cruises</h3>
  <p>Lorem ipsum dolor sit amet, consectetur adipiscing sed do eiusmod tempor incididunt ut</p>
  <div class="price">$50.00</div>
</article>

<!-- Highlighted destinations -->
<section class="dest-band" role="img" aria-label="Turquoise sea and sky backdrop"></section>
<h2 class="sec-title" style="top:1340px">HIGHLIGHTED <em>DESTINATIONS</em></h2>
<p class="dest-lead">Lorem ipsum dolor sit amet, consectetur adipiscing elit, sed do eiusmod tempor incidi dunt ut labore et dolore magna aliqua. Ut enim ad minim veniam, quis nostrud exercita</p>
<div class="dest" style="left:142px"><div class="dest-img" role="img" aria-label="Suspension bridge above a beach at sunset" style="background:linear-gradient(180deg,#9fb9cf 0%,#d19b77 55%,#e8cbb0 100%)"></div><h4>Lorem ipsum dolor</h4></div>
<div class="dest" style="left:453px"><div class="dest-img" role="img" aria-label="Traveller overlooking green island bays" style="background:linear-gradient(180deg,#4d8fcf 0%,#6b8f6a 55%,#2f7d8f 100%)"></div><h4>Lorem ipsum dolor</h4></div>
<div class="dest" style="left:764px"><div class="dest-img" role="img" aria-label="Two hikers walking a coastal cliff path in golden light" style="background:linear-gradient(160deg,#f1ecd0 0%,#c8c29a 50%,#6f7a45 100%)"></div><h4>Lorem ipsum dolor</h4></div>
<div class="arrow" style="left:52px;top:1581px;background:#fff"><svg viewBox="0 0 12 12"><path d="M8 1 L3 6 L8 11" stroke="#333" stroke-width="1.6" fill="none"/></svg></div>
<div class="arrow" style="left:1108px;top:1581px;background:#fff"><svg viewBox="0 0 12 12"><path d="M4 1 L9 6 L4 11" stroke="#333" stroke-width="1.6" fill="none"/></svg></div>

<!-- Cruise line highlights -->
<h2 class="sec-title" style="top:1892px">CRUISE LINE <em>HIGHLIGHTS</em></h2>
<article class="line-card" style="left:144px;top:1975px">
  <div class="line-img" role="img" aria-label="Yacht at sea during golden sunset" style="background:linear-gradient(180deg,#d9a560 0%,#b9a58a 50%,#4f6a80 100%)"></div>
  <h4>Lorem ipsum dolor sit</h4><p>Lorem ipsum dolor sit amet, consect etur adipiscing elit, sed do eiusmod tempor incidi dunt</p><a>Explore Now</a>
</article>
<article class="line-card" style="left:614px;top:1975px">
  <div class="line-img" role="img" aria-label="White superyacht on dark blue water" style="background:linear-gradient(180deg,#7f9fc4 0%,#3b5f8f 55%,#1c3c6e 100%)"></div>
  <h4>Lorem ipsum dolor sit</h4><p>Lorem ipsum dolor sit amet, consect etur adipiscing elit, sed do eiusmod tempor incidi dunt</p><a>Explore Now</a>
</article>
<article class="line-card" style="left:144px;top:2192px">
  <div class="line-img" role="img" aria-label="Excursion boat on the open sea" style="background:linear-gradient(180deg,#d5dfe8 0%,#8aa6bf 50%,#34618c 100%)"></div>
  <h4>Lorem ipsum dolor sit</h4><p>Lorem ipsum dolor sit amet, consect etur adipiscing elit, sed do eiusmod tempor incidi dunt</p><a>Explore Now</a>
</article>
<article class="line-card" style="left:614px;top:2192px">
  <div class="line-img" role="img" aria-label="Motor yacht speeding on turquoise water" style="background:linear-gradient(180deg,#57b0d3 0%,#1f8fc0 50%,#0d6ea6 100%)"></div>
  <h4>Lorem ipsum dolor sit</h4><p>Lorem ipsum dolor sit amet, consect etur adipiscing elit, sed do eiusmod tempor incidi dunt</p><a>Explore Now</a>
</article>
<div class="btn-more">View More Highlights</div>

<!-- Testimonials -->
<section class="testi-band" role="img" aria-label="Misty sea backdrop with a yacht at sunset"></section>
<h2 class="sec-title" style="top:2695px">CUSTOMER <em>TESTIMONIALS</em></h2>
<svg class="chev" style="left:56px" viewBox="0 0 24 30"><path d="M17 3 L7 15 L17 27" stroke="#222" stroke-width="2.5" fill="none"/></svg>
<svg class="chev" style="left:1116px" viewBox="0 0 24 30"><path d="M7 3 L17 15 L7 27" stroke="#222" stroke-width="2.5" fill="none"/></svg>
<article class="testi" style="left:215px">
  <div class="stars"><svg width="78" height="14" viewBox="0 0 78 14"><g fill="#f2a31b"><path id="star" d="M7 0 L8.8 4.8 L14 5.1 L10 8.4 L11.3 13.5 L7 10.6 L2.7 13.5 L4 8.4 L0 5.1 L5.2 4.8 Z"/><use href="#star" x="16"/><use href="#star" x="32"/><use href="#star" x="48"/><use href="#star" x="64"/></g></svg></div>
  <p>Lorem ipsum dolor sit amet, consectetur adipiscing elit, sed do eiusmod tempor incididunt ut labore et dolore magna aliqua.</p>
  <div class="who">John doe<small>Company name</small></div>
</article>
<div class="avatar" style="left:144px;background:linear-gradient(180deg,#c9b9a6,#9b8772)" role="img" aria-label="Customer portrait"></div>
<article class="testi" style="left:694px">
  <div class="stars"><svg width="78" height="14" viewBox="0 0 78 14"><g fill="#f2a31b"><use href="#star"/><use href="#star" x="16"/><use href="#star" x="32"/><use href="#star" x="48"/><use href="#star" x="64"/></g></svg></div>
  <p>Lorem ipsum dolor sit amet, consectetur adipiscing elit, sed do eiusmod tempor incididunt ut labore et dolore magna aliqua.</p>
  <div class="who">John doe<small>Company name</small></div>
</article>
<div class="avatar" style="left:623px;background:linear-gradient(180deg,#6fb8d8,#3a7fae)" role="img" aria-label="Customer portrait"></div>

<!-- Footer -->
<svg class="footer-wave" viewBox="0 0 1200 100" preserveAspectRatio="none"><path d="M0 65 C150 70 250 40 380 30 C520 20 560 55 680 60 C800 65 840 10 960 15 C1060 20 1120 60 1200 70 L1200 100 L0 100 Z" fill="#2b2a6b"/></svg>
<footer class="footer">
  <h5 style="left:144px;top:86px">SUBSCRIBE TO<br>OUR NEWSLETTER</h5>
  <div class="email-field">Email address<svg width="16" height="16" viewBox="0 0 16 16"><path d="M1 8 L15 1 L11 15 L8 9 Z" fill="#fff"/></svg></div>
  <span class="social" style="left:147px"></span>
  <span class="social on" style="left:177px"></span>
  <span class="social" style="left:212px"></span>

  <h5 style="left:504px;top:86px">CONTACT INFO</h5>
  <div class="contact-item" style="top:132px"><svg width="14" height="18" viewBox="0 0 14 18"><path d="M7 0 C3 0 0 3 0 7 C0 12 7 18 7 18 C7 18 14 12 14 7 C14 3 11 0 7 0 Z M7 4 A3 3 0 1 1 7 10 A3 3 0 1 1 7 4 Z" fill="#fff" fill-rule="evenodd"/></svg><strong>Address</strong><span>Lorem ipsum dolor sit amet</span></div>
  <div class="contact-item" style="top:188px"><svg width="20" height="14" viewBox="0 0 20 14"><rect width="20" height="14" rx="1" fill="#fff"/><path d="M0 1 L10 8 L20 1" stroke="#2b2a6b" stroke-width="1.6" fill="none"/></svg><strong>Email</strong><span>info@companyname.com</span></div>
  <div class="contact-item" style="top:245px"><svg width="18" height="18" viewBox="0 0 18 18"><path d="M4 0 L7 5 L5 7 C6 10 8 12 11 13 L13 11 L18 14 L16 18 C8 18 0 10 0 2 Z" fill="#fff"/></svg><strong>Phone</strong><span>+1 888 888 8888</span></div>

  <h5 style="left:766px;top:86px">QUICK LINKS</h5>
  <ul class="links" style="left:766px"><li>Home</li><li>About</li><li>Services</li><li>Contact</li></ul>
  <ul class="links" style="left:902px"><li>Terms and Condition</li><li>Privacy policy</li><li>Help</li><li>Support</li></ul>

  <div class="copyright">© Copyrights 2025 | All Rights Reserved</div>
</footer>

</body>
</html>
```